Need new sign at entrance for new fruit and vegetable wholesaler in market. Main vegetables sold are
Broccoli , Cauliflower , cabbage , capsicum , tomatoes , lettuce .
Business name is Tall Meadow
I have included examples of other designs and a sketch of suggested layout.

```html
<!DOCTYPE html>
<html lang="en">
<head>
<meta charset="utf-8">
<title>Tall Meadow – Entrance Sign</title>
<link rel="stylesheet" href="https://fonts.googleapis.com/css2?family=Archivo+Black&display=swap">
<style>
  :root {
    --page-bg: #f2f2f2;
    --sign-green: #3e9b0c;
    --sign-green-light: #4aab12;
    --sign-green-dark: #1f6a08;
    --name-yellow: #ffe21a;
    --badge-red: #e21a22;
    --contact-red: #e3132a;
    --white: #ffffff;
  }
  * { margin: 0; padding: 0; box-sizing: border-box; }
  html, body {
    width: 1200px;
    height: 833px;
    overflow: hidden;
  }
  body {
    background: linear-gradient(180deg, #ededed 0%, var(--page-bg) 30%, #f7f7f7 100%);
    position: relative;
    font-family: "Archivo Black", "Arial Black", sans-serif;
  }
  .entrance-sign {
    position: absolute;
    left: 44px;
    top: 305px;
    width: 1112px;
    height: 222px;
    background: radial-gradient(ellipse at 55% 50%, var(--sign-green-light) 0%, var(--sign-green) 60%, #358a0a 100%);
    overflow: hidden;
  }
  .produce-panel {
    position: absolute;
    left: 0;
    top: 0;
    width: 400px;
    height: 222px;
  }
  .brand-name {
    position: absolute;
    left: 592px;
    top: 111px;
    transform: translate(-50%, -50%);
    display: flex;
    align-items: center;
    gap: 12px;
  }
  .brand-name .brand-dot {
    flex: none;
    width: 30px;
    height: 30px;
    border-radius: 50%;
    background: var(--badge-red);
  }
  .brand-name .brand-text {
    color: var(--name-yellow);
    font-size: 46px;
    line-height: 1.05;
    text-align: center;
    white-space: nowrap;
  }
  .contact-block {
    position: absolute;
    right: 26px;
    top: 56px;
    text-align: right;
    color: var(--contact-red);
    font-size: 23px;
    line-height: 36px;
    white-space: nowrap;
    -webkit-text-stroke: 5px var(--white);
    paint-order: stroke fill;
  }
</style>
</head>
<body>
  <section class="entrance-sign">
    <svg class="produce-panel" viewBox="0 0 400 222" role="img" aria-label="Photo of fresh vegetables: cauliflower, broccoli, tomatoes, capsicum, onion and potato">
      <defs>
        <linearGradient id="produceTones" x1="0" y1="0" x2="1" y2="1">
          <stop offset="0" stop-color="#e9e6cf"/>
          <stop offset="0.35" stop-color="#5f9a2c"/>
          <stop offset="0.6" stop-color="#c8421e"/>
          <stop offset="0.85" stop-color="#f0a21a"/>
          <stop offset="1" stop-color="#d8c35a"/>
        </linearGradient>
      </defs>
      <path d="M0,0 H300 Q372,90 378,222 H0 Z" fill="url(#produceTones)"/>
      <path d="M300,0 Q372,90 378,222" fill="none" stroke="var(--sign-green-dark)" stroke-width="9"/>
    </svg>

    <div class="brand-name">
      <span class="brand-dot"></span>
      <span class="brand-text">TALL<br>MEADOW</span>
    </div>

    <div class="contact-block">
      <p class="contact-web">www.tallmeadow.com</p>
      <p class="contact-phone">Phone - 02 5550 1928</p>
      <p class="contact-fax">Fax - 02 5550 1928</p>
    </div>
  </section>
</body>
</html>
```